Create a 3-4 page concept for an electrical contracting company

We are a company that requires a new look for our website. We are familiar with Sitecraft to be able to update using any theme or builder supplied.

While typical ideas of construction may get the yellow and blue colour pallette, hard hats, hammers, or lightning bolts entering the arena, we are completely against this image.

We intend for the website to have instant appeal and intuitive navigation. The home page should have a creative use of angles or brand identification with the banner or menubar if needed.

After combing hundreds of sitecraft templates, the most attractive seem to be aimed at beauty services. Unfortunately we do not have a lot of picture perfect material to showcase, but it can be blended in other ways. - the brand should be recognizable and captivating.

Target Market(s)

High-end contracting firms focused on quality and service for long term projects (Custom Homes)

Industry/Entity Type

Contracting

Font styles to use
Sans Serif
Other font styles liked:
• Gotham usually. Adjusted kerning and rounded edges seem to be more friendly

Requirements
Must have
• Creative use of the logo shape and colour scheme, especially at the home.

Use of a CMS to be modifiable from a browser (Sitecraft,etc) - A builder such as tandem, kora, or framewell accepted!

Elements or sections that could be adaptable for use. About us, members, contact, services... etc. Content would be written after
Nice to have
• Some clean inspiration that we appreciate:

www.harbelmedia.ca
www.pinwoodbuildworks.com
Should not have
• Generic welcome banner...

```html
<!DOCTYPE html>
<html lang="en">
<head>
<meta charset="utf-8">
<title>Norwell Wiring</title>
<link rel="stylesheet" href="https://fonts.googleapis.com/css2?family=Montserrat:wght@200;300;400;500;600;700;800&display=swap">
<style>
:root{
  --blue:#2a84c2;
  --blue-deep:#1d6aa3;
  --steel:#3b4a57;
  --ink:#1d1f22;
  --text:#3a3d42;
  --mist:#f6f7f9;
  --footer:#252628;
  --white:#ffffff;
}
html,body{margin:0;padding:0;overflow:hidden;background:var(--white);}
body{font-family:"Montserrat",Arial,sans-serif;color:var(--text);}
.page{position:relative;width:1200px;height:3528px;overflow:hidden;background:var(--white);}
.abs{position:absolute;}
.center-line{left:0;width:1200px;text-align:center;}
svg.layer{position:absolute;left:0;top:0;}

/* Header */
.brand{display:flex;align-items:center;gap:12px;color:var(--white);font-weight:600;font-size:20px;line-height:24px;letter-spacing:1px;white-space:nowrap;}
.brand-dot{width:14px;height:14px;border-radius:50%;background:var(--white);}
.nav{top:47px;left:458px;font-size:13px;color:var(--white);font-weight:400;}
.nav span{position:absolute;white-space:nowrap;}
.nav-cta{left:922px;top:36px;width:129px;height:38px;background:var(--blue);color:var(--white);font-size:13px;line-height:38px;text-align:center;}

.hero-photo{left:0;top:0;width:1200px;height:670px;background:linear-gradient(160deg,#20252c 0%,#3a3530 35%,#5a4128 55%,#2a2a2e 80%,#1c1f24 100%);}
.hero-title{top:272px;font-size:56px;font-weight:200;color:var(--white);letter-spacing:2px;}
.hero-sub{top:352px;font-size:12.5px;line-height:22px;color:var(--white);font-weight:500;}
.btn-solid{background:var(--blue);color:var(--white);font-size:13px;text-align:center;}
.hero-btn{left:536px;top:410px;width:128px;height:37px;line-height:37px;}
.vline{left:600px;top:137px;width:1px;height:123px;background:rgba(255,255,255,.7);}
.dots-nav span{position:absolute;left:1100px;width:14px;height:14px;border:1.5px solid var(--white);box-sizing:border-box;}

/* About */
.soft-blob{background:radial-gradient(circle,rgba(180,186,194,.22) 0%,rgba(180,186,194,0) 70%);border-radius:50%;}
.eyebrow{font-size:16px;color:var(--ink);font-weight:400;letter-spacing:.5px;}
.about-title{left:162px;top:720px;font-size:33px;font-weight:700;letter-spacing:7px;color:var(--ink);white-space:nowrap;}
.about-copy{left:162px;top:786px;width:440px;font-size:10.6px;line-height:24px;color:var(--ink);letter-spacing:-.15px;}
.about-copy p{margin:0 0 24px;}
.about-btn{left:162px;top:1005px;width:128px;height:39px;line-height:39px;}
.about-visual{left:651px;top:723px;width:338px;height:389px;background:linear-gradient(170deg,#4d8cd0 0%,#9aa7ae 35%,#6b5a48 60%,#2f3a2c 85%,#4b7c36 100%);box-shadow:0 12px 24px rgba(0,0,0,.25);}

/* Services */
.sv-eyebrow{top:1243px;font-size:15px;color:var(--white);}
.sv-title{top:1270px;font-size:32px;font-weight:700;letter-spacing:6px;color:var(--white);}
.sv-copy{top:1329px;font-size:12.5px;line-height:22px;color:var(--white);}
.card{top:1429px;width:289px;height:399px;background:var(--white);box-shadow:0 6px 18px rgba(0,0,0,.22);}
.card-photo{position:absolute;left:10px;top:10px;width:269px;height:168px;}
.card h3{position:absolute;top:204px;left:0;width:289px;margin:0;text-align:center;font-size:18px;font-weight:600;color:var(--ink);letter-spacing:.3px;}
.card p{position:absolute;top:238px;left:14px;width:261px;margin:0;text-align:center;font-size:9.8px;line-height:19.5px;color:var(--text);letter-spacing:-.15px;}
.card-btn{position:absolute;left:91px;top:337px;width:107px;height:32px;border:1px solid var(--blue);box-sizing:border-box;color:var(--blue);font-size:11px;line-height:30px;text-align:center;}

/* Testimonials */
.ts-eyebrow{top:2020px;font-size:16px;color:var(--ink);}
.ts-title{top:2052px;font-size:32px;line-height:51px;font-weight:700;color:var(--ink);letter-spacing:.5px;}
.ts-frame{left:166px;top:2244px;width:198px;height:212px;background:var(--blue);border-radius:18px 0 18px 18px;}
.ts-photo{left:186px;top:2212px;width:200px;height:213px;border-radius:22px;background:linear-gradient(150deg,#8fb7d2 0%,#b79a73 40%,#6d5a46 70%,#cbd3da 100%);}
.ts-quote{left:430px;top:2240px;width:590px;font-size:11.6px;line-height:31.5px;color:var(--text);letter-spacing:-.1px;}
.ts-name{left:430px;top:2387px;font-size:23px;font-weight:700;color:var(--ink);}
.ts-name small{font-size:12px;font-weight:400;color:var(--text);}
.ts-arrow{width:32px;height:32px;}

/* Portfolio */
.pf-eyebrow{top:2615px;font-size:16px;color:var(--ink);}
.pf-title{top:2651px;font-size:32px;font-weight:700;color:var(--ink);letter-spacing:1px;}
.pf-item{overflow:hidden;}
.pf-caption{position:absolute;left:0;bottom:0;width:100%;height:52px;background:rgba(40,60,80,.45);color:var(--white);font-weight:700;letter-spacing:3px;font-size:17px;line-height:52px;box-sizing:border-box;}

/* Newsletter + footer */
.news{left:0;top:3178px;width:1200px;height:58px;background:var(--blue);}
.news-label{left:190px;top:3197px;color:var(--white);font-weight:600;font-size:15px;letter-spacing:2.5px;}
.news-input{left:600px;top:3186px;width:348px;height:40px;background:var(--white);font-size:9px;color:#9aa0a6;line-height:40px;padding-left:14px;box-sizing:border-box;}
.news-send{left:955px;top:3186px;width:103px;height:40px;background:var(--steel);color:var(--white);font-weight:600;font-size:14px;line-height:40px;text-align:center;}
.footer{left:0;top:3236px;width:1200px;height:292px;background:var(--footer);}
.ft-head{top:3262px;color:var(--white);font-size:20px;font-weight:500;letter-spacing:4px;}
.ft-links{left:585px;top:3316px;margin:0;padding:0;list-style:none;color:var(--white);font-size:11px;}
.ft-links li{height:27px;line-height:20px;}
.ft-links li::before{content:"✓";font-size:9px;margin-right:8px;}
.ft-contact{left:830px;top:3316px;color:var(--white);font-size:11px;}
.ft-contact div{display:flex;align-items:center;gap:10px;height:36px;line-height:20px;}
.ft-rule{left:455px;top:3463px;width:603px;height:1px;background:rgba(255,255,255,.6);}
.ft-copy{left:700px;top:3485px;width:352px;text-align:right;color:var(--white);font-size:10.5px;}
.social{top:3396px;width:30px;height:30px;border-radius:50%;background:var(--blue);}
</style>
</head>
<body>
<div class="page">

  <!-- Hero -->
  <div class="abs hero-photo" role="img" aria-label="Dusk photograph of a modern timber custom home with warm lit windows and front steps"></div>
  <svg class="layer" width="1200" height="680" viewBox="0 0 1200 680" aria-hidden="true">
    <polygon points="0,560 1200,605 1200,680 0,680" fill="#ffffff"/>
    <polygon points="0,558 1200,600 1200,650 0,566" fill="#2a84c2"/>
    <polygon points="0,566 1200,650 1200,680 0,680" fill="#ffffff"/>
  </svg>

  <div class="abs brand" style="left:165px;top:43px;">
    <span class="brand-dot"></span>
    <span>NORWELL WIRING</span>
  </div>
  <nav class="abs nav">
    <span style="left:0;">HOME</span>
    <span style="left:83px;">ABOUT US</span>
    <span style="left:194px;">SERVICES</span>
    <span style="left:301px;">TESTIMONIALS</span>
    <span style="left:410px;">|</span>
  </nav>
  <svg class="abs" style="left:885px;top:47px;" width="18" height="18" viewBox="0 0 18 18" aria-hidden="true">
    <circle cx="7.5" cy="7.5" r="5.5" fill="none" stroke="#fff" stroke-width="1.4"/>
    <line x1="11.5" y1="11.5" x2="16" y2="16" stroke="#fff" stroke-width="1.4"/>
  </svg>
  <div class="abs nav-cta">CONTACT US</div>

  <div class="abs vline"></div>
  <div class="abs center-line hero-title">NORWELL WIRING</div>
  <div class="abs center-line hero-sub">Maecenas volutpat lacinia purus, vitae porta massa vulputate at. Nulla ac tristique nisl. Nam facilisis,<br>tellus quis interdum tincidunt, tellus magna vehicula neque</div>
  <div class="abs btn-solid hero-btn">Learn More</div>
  <svg class="abs" style="left:590px;top:498px;" width="20" height="42" viewBox="0 0 20 42" aria-hidden="true">
    <rect x="3" y="1" width="14" height="20" rx="7" fill="none" stroke="#fff" stroke-width="1.3"/>
    <line x1="10" y1="5" x2="10" y2="9" stroke="#fff" stroke-width="1.3"/>
    <polyline points="4,27 10,32 16,27" fill="none" stroke="#fff" stroke-width="1.3"/>
    <polyline points="4,33 10,38 16,33" fill="none" stroke="#fff" stroke-width="1.3"/>
  </svg>
  <div class="dots-nav">
    <span style="top:295px;background:#fff;"></span>
    <span style="top:320px;"></span>
    <span style="top:345px;"></span>
  </div>

  <!-- About -->
  <div class="abs soft-blob" style="left:90px;top:580px;width:330px;height:200px;"></div>
  <div class="abs soft-blob" style="left:880px;top:1010px;width:320px;height:200px;"></div>
  <div class="abs eyebrow" style="left:162px;top:693px;">ABOUT</div>
  <div class="abs about-title">NORWELL WIRING</div>
  <div class="abs about-copy">
    <p>Integer sagittis metus vitae diam dignissim, at gravida nisi feugiat. Suspendisse non nisi sollicitudin, egestas mi sit amet, porta nisl. Phasellus quis convallis odio, ac gravida orci.</p>
    <p>&nbsp;Suspendisse pharetra tristique mauris, ac ornare justo. Sed maximus ullamcorper felis et faucibus. Vestibulum eu dui sapien. Nulla dictum odio mauris, ac fermentum quam faucibus congue. Quisque id convallis dolor, sed faucibus urna. Suspendisse ante neque, gravida eget lobortis vel, rutrum eu tortor.</p>
  </div>
  <div class="abs btn-solid about-btn">Learn More</div>
  <div class="abs about-visual" role="img" aria-label="Collage of modern luxury homes with glass balconies, stone walls and a lawn"></div>

  <!-- Services band -->
  <svg class="layer" width="1200" height="2600" viewBox="0 0 1200 2600" aria-hidden="true">
    <defs>
      <linearGradient id="bandTone" x1="0" y1="0" x2="1" y2="1">
        <stop offset="0" stop-color="#2a7cb6"/>
        <stop offset=".5" stop-color="#2a86c4"/>
        <stop offset="1" stop-color="#2f8fcc"/>
      </linearGradient>
    </defs>
    <polygon points="0,1950 1200,1896 1200,2590 0,2521" fill="#f6f7f9"/>
    <polygon points="0,1140 1200,1170 1200,1182 0,1148" fill="#3b4a57"/>
    <polygon points="0,1148 1200,1182 1200,1888 0,1942" fill="url(#bandTone)"/>
    <polygon points="0,1942 1200,1888 1200,1898 0,1952" fill="#3b4a57"/>
  </svg>
  <div class="abs" style="left:0;top:1180px;width:1200px;height:700px;background:linear-gradient(100deg,rgba(20,60,100,.18),rgba(255,255,255,0) 45%,rgba(20,60,100,.15));" role="img" aria-label="Faint tinted photograph of palm trees and a villa behind the services section"></div>

  <div class="abs center-line sv-eyebrow">OUR SERVICES</div>
  <div class="abs center-line sv-title">WHAT WE DO</div>
  <div class="abs center-line sv-copy">Sed egestas dui augue, vitae hendrerit nunc commodo quis. Duis eu porta metus. Vestibulum quam leo, laoreet at euismod sed,<br>pulvinar ut odio. Vivamus porta elementum purus, ut blandit ex varius at.</div>

  <article class="abs card" style="left:141px;">
    <div class="card-photo" role="img" aria-label="Modern multi-level home with wooden louvres and glass balconies" style="background:linear-gradient(165deg,#c9ccc8 0%,#8f8578 45%,#5b5148 75%,#3e3a35 100%);"></div>
    <h3>New Custom Homes</h3>
    <p>Pellentesque fringilla interdum condimentum. Morbi sagittis, tellus id varius ornare, arcu tortor consectetur est, sed imperdiet mauris ligula luctus nisi. Donec feugiat orci</p>
    <div class="card-btn">Learn More</div>
  </article>
  <article class="abs card" style="left:455px;">
    <div class="card-photo" role="img" aria-label="Team reviewing plans on a laptop at a white desk" style="background:linear-gradient(160deg,#f0f0f0 0%,#d6d6d6 45%,#5a5a5a 65%,#e8e8e8 100%);"></div>
    <h3>Project Managment</h3>
    <p>Pellentesque fringilla interdum condimentum. Morbi sagittis, tellus id varius ornare, arcu tortor consectetur est, sed imperdiet mauris ligula luctus nisi. Donec feugiat orci a ante rhoncus</p>
    <div class="card-btn">Learn More</div>
  </article>
  <article class="abs card" style="left:769px;">
    <div class="card-photo" role="img" aria-label="Bright renovated open-plan interior with dark sofas" style="background:linear-gradient(170deg,#d9d9d7 0%,#b5b3ae 45%,#4a4642 80%,#2f2c29 100%);"></div>
    <h3>Commercial Renovations</h3>
    <p>Pellentesque fringilla interdum condimentum. Morbi sagittis, tellus id varius ornare, arcu tortor consectetur est, sed imperdiet mauris ligula luctus nisi. Donec feugiat orci a ante rhoncus</p>
    <div class="card-btn">Learn More</div>
  </article>

  <!-- Testimonials -->
  <div class="abs soft-blob" style="left:830px;top:1960px;width:310px;height:220px;"></div>
  <div class="abs soft-blob" style="left:125px;top:2120px;width:320px;height:210px;"></div>
  <div class="abs center-line ts-eyebrow">Our Testimonials</div>
  <div class="abs center-line ts-title">LET’S SEE OUR AWESOME<br>CLIENT’S REVIEWS</div>
  <div class="abs ts-frame"></div>
  <div class="abs ts-photo" role="img" aria-label="Portrait of a smiling client in a beanie holding a phone on a city street"></div>
  <div class="abs ts-quote">Nullam ut tortor consectetur, sodales sapien quis, gravida lorem. Aenean porttitor molestie tellus, vel sollicitudin ligula consequat id. Donec varius mauris in cursus mollis. Donec vitae tincidunt sapien. Ut eget enim vel felis vulputate vehicula. Fusce pulvinar, ante eu dictum ornare, augue dui efficitur elit, cursus malesuada est lacus quis velit.</div>
  <div class="abs ts-name">Name Here <small>/ Director</small></div>
  <svg class="abs ts-arrow" style="left:84px;top:2328px;" viewBox="0 0 32 32" aria-hidden="true">
    <circle cx="16" cy="16" r="15" fill="none" stroke="#555" stroke-width="1.2"/>
    <polyline points="17,9 10,16 17,23" fill="none" stroke="#555" stroke-width="1.2"/>
    <polyline points="22,9 15,16 22,23" fill="none" stroke="#555" stroke-width="1.2"/>
  </svg>
  <svg class="abs ts-arrow" style="left:1091px;top:2328px;" viewBox="0 0 32 32" aria-hidden="true">
    <circle cx="16" cy="16" r="15" fill="none" stroke="#555" stroke-width="1.2"/>
    <polyline points="15,9 22,16 15,23" fill="none" stroke="#555" stroke-width="1.2"/>
    <polyline points="10,9 17,16 10,23" fill="none" stroke="#555" stroke-width="1.2"/>
  </svg>

  <!-- Portfolio -->
  <div class="abs center-line pf-eyebrow">Portfolio</div>
  <div class="abs center-line pf-title">OUR WORK</div>
  <div class="abs pf-item" style="left:0;top:2774px;width:274px;height:313px;background:linear-gradient(180deg,#6e6a9a 0%,#b58a7a 35%,#5a4a40 60%,#2b4a70 100%);" role="img" aria-label="Hillside home at dusk with a lit pool deck">
    <div class="pf-caption" style="padding-left:0;text-indent:-22px;">Title Here</div>
  </div>
  <div class="abs pf-item" style="left:299px;top:2745px;width:602px;height:369px;background:linear-gradient(180deg,#bfe0f2 0%,#d9c9a8 35%,#a78a62 55%,#3aa0c8 75%,#1f7fb0 100%);" role="img" aria-label="Large Mediterranean-style villa with terracotta roofs and a blue pool">
    <div class="pf-caption" style="height:58px;line-height:58px;padding-left:42px;font-size:20px;">Title Here</div>
  </div>
  <div class="abs pf-item" style="left:925px;top:2774px;width:275px;height:313px;background:linear-gradient(180deg,#4a6a9a 0%,#c9a0a0 35%,#4b4f58 60%,#4e7a3a 100%);" role="img" aria-label="Oceanfront modern home at sunset with a lawn and pool">
    <div class="pf-caption" style="padding-left:30px;">Title Here</div>
  </div>

  <!-- Newsletter -->
  <div class="abs news"></div>
  <svg class="abs" style="left:158px;top:3193px;" width="28" height="28" viewBox="0 0 28 28" aria-hidden="true">
    <circle cx="14" cy="14" r="14" fill="#fff"/>
    <polygon points="8,14 20,8 16,20 14,15" fill="none" stroke="#2a84c2" stroke-width="1.3" stroke-linejoin="round"/>
  </svg>
  <div class="abs news-label">Subscribe To Newsletter</div>
  <div class="abs news-input">Send a Message...</div>
  <div class="abs news-send">Send &nbsp;⟶</div>

  <!-- Footer -->
  <footer class="abs footer"></footer>
  <div class="abs brand" style="left:167px;top:3318px;font-size:21px;">
    <span class="brand-dot"></span>
    <span>NORWELL WIRING</span>
  </div>
  <span class="abs social" style="left:211px;" role="img" aria-label="Social profile link"></span>
  <span class="abs social" style="left:251px;" role="img" aria-label="Social profile link"></span>
  <span class="abs social" style="left:292px;" role="img" aria-label="Social profile link"></span>

  <div class="abs ft-head" style="left:577px;">Quick Links</div>
  <ul class="abs ft-links">
    <li>Home</li>
    <li>About Us</li>
    <li>Our Services</li>
    <li>Testimonials</li>
    <li>Portfolio</li>
  </ul>

  <div class="abs ft-head" style="left:821px;">Get In Touch</div>
  <div class="abs ft-contact">
    <div>
      <svg width="12" height="12" viewBox="0 0 12 12" aria-hidden="true"><path d="M2.5 1 L4.5 1 L5.3 3.5 L4 4.6 C4.7 6.1 5.9 7.3 7.4 8 L8.5 6.7 L11 7.5 L11 9.5 C11 10.4 10.3 11 9.5 11 C5 11 1 7 1 2.5 C1 1.7 1.6 1 2.5 1 Z" fill="#fff"/></svg>
      <span>88-888-8888</span>
    </div>
    <div>
      <svg width="12" height="12" viewBox="0 0 12 12" aria-hidden="true"><rect x="1" y="2.5" width="10" height="7" fill="#fff"/><polyline points="1,2.5 6,6.5 11,2.5" fill="none" stroke="#252628" stroke-width="1"/></svg>
      <span>Info@yourmail.com</span>
    </div>
    <div>
      <svg width="12" height="12" viewBox="0 0 12 12" aria-hidden="true"><path d="M6 0.8 C3.8 0.8 2.2 2.4 2.2 4.5 C2.2 7.3 6 11.2 6 11.2 C6 11.2 9.8 7.3 9.8 4.5 C9.8 2.4 8.2 0.8 6 0.8 Z" fill="#fff"/><circle cx="6" cy="4.5" r="1.4" fill="#252628"/></svg>
      <span>123 dummy text456</span>
    </div>
  </div>

  <div class="abs ft-rule"></div>
  <div class="abs ft-copy">© 2020 Norwell Wiring - ALL RIGHTS RESERVED.</div>

</div>
</body>
</html>
```